Beautiful design for wordpress

I need a beautiful, colourful and feminine website. My business is called 'The Velvet Lantern', and I sell crystals, books, CD's, pendulums and other metaphysical items. I also provide Reiki (energy healing).
I want this design to be eye catching and inspire happiness and joy in those who see it. And I would love to see the use of the logo and its colours :)
Please add these on the web design: Home, About, Online store, Blog

Must have
• Colourful and playful, must use the logo somewhere, have the words on a menu saying 'Home, Blog, Online store and about' (or similar to those)And the design must stand out!
Should not have
• grey, brown and other boring colours.

```html
<!DOCTYPE html>
<html lang="en">
<head>
<meta charset="utf-8">
<title>The Velvet Lantern — Crystals &amp; Gifts</title>
<link rel="stylesheet" href="https://fonts.googleapis.com/css2?family=Playfair+Display:ital,wght@1,400;1,700&family=Roboto+Slab:wght@300;400;700&family=Roboto:wght@400;500&display=swap">
<style>
:root{
  --pink:#e91e7a;
  --pink-soft:#ee4b8f;
  --orange:#f7a23b;
  --page-bg:#f4e4ea;
  --panel:#f6f6f6;
  --ink:#2b2b2b;
  --muted:#666;
  --white:#fff;
  --line:#dcdcdc;
}
*{box-sizing:border-box;margin:0;padding:0}
html,body{width:1200px;height:2941px;overflow:hidden}
body{background:var(--page-bg);font-family:"Roboto",Arial,sans-serif;color:var(--ink)}
.canvas{position:relative;width:1200px;height:2941px;overflow:hidden}
.abs{position:absolute}

/* utility bar */
.account-bar{left:92px;top:0;height:30px;width:360px;background:var(--orange);border-radius:0 0 14px 14px;display:flex;align-items:center;padding:0 24px;color:var(--white);font-size:15px}
.account-bar span{padding:0 18px;border-right:1px solid rgba(255,255,255,.6)}
.account-bar span:first-child{padding-left:0}
.account-bar span:last-child{border-right:none}
.caret{display:inline-block;border:5px solid transparent;border-top-color:var(--white);margin-left:6px;vertical-align:-2px}
.help-call{right:92px;top:22px;text-align:right;color:var(--orange);font-family:"Roboto",sans-serif}
.help-call .q{font-size:23px}
.help-call .num{font-size:33px;font-weight:500;line-height:1.1}

/* navigation */
.main-nav{left:92px;top:108px;width:1016px;height:43px;background:var(--pink);border-radius:12px;z-index:2}
.main-nav a{position:absolute;top:0;line-height:43px;color:var(--white);text-decoration:none;font-size:15px;text-transform:uppercase;text-align:center}
.nav-sep{position:absolute;top:9px;width:1px;height:25px;background:rgba(255,255,255,.45)}
.brand{left:518px;top:50px;width:164px;height:164px;border-radius:50%;background:var(--white);box-shadow:0 2px 8px rgba(0,0,0,.15);display:flex;align-items:center;justify-content:center;text-align:center;color:var(--pink);font-family:"Roboto Slab",serif;font-weight:700;font-size:22px;line-height:1.15;padding:20px;z-index:5}

/* hero */
.hero{left:92px;top:157px;width:1016px;height:353px;background:linear-gradient(100deg,#e8f0d8 0%,#f4f2ea 45%,#fbf7f4 100%)}
.hero-art{left:100px;top:170px;width:420px;height:330px;border-radius:8px;background:radial-gradient(ellipse at 50% 55%,#9fcf54 0%,#e670b5 45%,rgba(240,240,230,0) 75%)}
.hero-title{left:480px;top:268px;width:605px;text-align:right;white-space:nowrap;color:var(--pink);font-family:"Playfair Display",serif;font-style:italic;font-weight:700;font-size:42px;line-height:1.2}
.hero-sub{left:560px;top:328px;width:500px;text-align:center;font-size:14px;color:#444;line-height:1.3}
.btn-detail{left:716px;top:410px;width:152px;height:50px;border-radius:24px;background:var(--pink);color:var(--white);font-family:"Playfair Display",serif;font-style:italic;font-size:16px;text-transform:uppercase;display:flex;align-items:center;justify-content:center}

/* panel */
.panel{left:92px;top:510px;width:1016px;height:2010px;background:var(--panel)}
.intro{left:180px;top:552px;width:840px;text-align:center;font-family:"Roboto Slab",serif;font-size:21px;line-height:1.35;color:var(--ink)}
.inspire{left:240px;top:632px;width:720px;text-align:center;font-family:"Playfair Display",serif;font-style:italic;font-size:31px;line-height:1.25;color:var(--pink-soft)}
.rule{height:1px;background:var(--line)}

/* categories */
.category{width:300px;text-align:center}
.category .ring{width:230px;height:230px;margin:0 auto;border-radius:50%;border:10px solid;display:flex;align-items:center;justify-content:center;background:var(--white)}
.category .photo{width:196px;height:196px;border-radius:50%}
.category h3{margin-top:26px;font-family:"Playfair Display",serif;font-style:italic;font-weight:400;font-size:20px;letter-spacing:1px;color:#444;text-transform:uppercase}
.category p{margin-top:14px;font-size:14px;line-height:1.3;color:var(--muted)}

/* section ribbons */
.ribbon{width:272px;height:84px;border-radius:22px;background:var(--pink);color:var(--white);font-family:"Playfair Display",serif;font-style:italic;font-size:22px;text-transform:uppercase;display:flex;align-items:center;justify-content:center}
.products-lead{left:150px;top:1400px;width:900px;text-align:center;font-family:"Roboto Slab",serif;font-size:21px;line-height:1.35}

/* products */
.product{width:170px;text-align:center}
.product .ring{width:165px;height:165px;margin:0 auto;border-radius:50%;border:9px solid;background:var(--white);display:flex;align-items:center;justify-content:center}
.product .photo{width:128px;height:128px;border-radius:50%}
.product .tag{margin:-16px auto 0;width:150px;height:50px;border-radius:18px;color:var(--white);font-family:"Roboto Slab",serif;font-weight:700;font-size:15px;line-height:1.2;display:flex;flex-direction:column;align-items:center;justify-content:center;position:relative}

/* map */
.map{left:92px;top:2205px;width:1016px;height:313px;background:linear-gradient(135deg,#e9ecd9 0%,#f3efe2 40%,#dfe8d2 70%,#eef0e4 100%)}
.address{left:190px;top:2250px;width:240px;height:240px;border-radius:50%;background:var(--orange);color:var(--white);font-family:"Roboto Slab",serif;font-weight:700;text-align:center;display:flex;flex-direction:column;align-items:center;justify-content:center;font-size:24px;line-height:1.25}
.address .who{color:var(--pink)}

/* contact */
.contact{left:92px;top:2518px;width:1016px;height:328px;background:var(--pink)}
.field{position:absolute;border:1px solid rgba(255,255,255,.75);border-radius:3px;color:var(--white);font-size:13px;padding:10px 12px}
.btn-send{left:355px;top:2773px;width:278px;height:44px;background:var(--white);color:var(--pink);font-family:"Roboto Slab",serif;font-size:17px;text-transform:uppercase;display:flex;align-items:center;justify-content:center;border-radius:2px}
.contact-copy{left:692px;top:2582px;width:380px;color:var(--white)}
.contact-copy h2{font-family:"Roboto Slab",serif;font-weight:400;font-size:28px}
.contact-copy p{margin-top:8px;font-size:14px;line-height:1.3}
.contact-copy ul{margin-top:14px;list-style:none}
.contact-copy li{font-size:15px;line-height:28px;padding-left:28px;position:relative}
.contact-copy li::before{content:"";position:absolute;left:2px;top:9px;width:11px;height:11px;border-radius:50%;background:var(--white)}

/* footer */
.footer{left:92px;top:2846px;width:1016px;height:95px;background:var(--white);text-align:center;font-size:14px;color:var(--muted);padding-top:42px}
</style>
</head>
<body>
<div class="canvas">

  <div class="abs account-bar">
    <span>My Account<i class="caret"></i></span><span>Help</span><span>Wish List<i class="caret"></i></span>
  </div>
  <div class="abs help-call">
    <div class="q">Need help planning?</div>
    <div class="num">(555) 218-0934</div>
  </div>

  <nav class="abs main-nav">
    <a href="#" style="left:0;width:170px">Home</a>
    <span class="nav-sep" style="left:170px"></span>
    <a href="#" style="left:170px;width:180px">About</a>
    <a href="#" style="left:666px;width:170px">Blog</a>
    <span class="nav-sep" style="left:836px"></span>
    <a href="#" style="left:836px;width:180px">Online Store</a>
  </nav>

  <section class="abs hero"></section>
  <div class="abs hero-art" role="img" aria-label="Photo of a green gift box tied with a pink polka-dot ribbon"></div>
  <h1 class="abs hero-title">Lorem ipsum dolor sit amet</h1>
  <p class="abs hero-sub">Duis autem vel eum iriure dolor in hendrerit in vulputate velit esse molestie consequat, vel illum dolore</p>
  <div class="abs btn-detail">More Detail</div>

  <div class="abs brand">The Velvet Lantern</div>

  <div class="abs panel"></div>
  <p class="abs intro">A unique way to spice up your event with a creative display of custom designed sweets &amp; deserts for any occasion.</p>
  <p class="abs inspire">Get inspired, take a look at our featured sweets below...</p>
  <div class="abs rule" style="left:118px;top:742px;width:964px"></div>

  <div class="abs category" style="left:110px;top:805px">
    <div class="ring" style="border-color:var(--orange)"><div class="photo" role="img" aria-label="Photo of a stack of colourful books" style="background:radial-gradient(circle,#e4556a,#7fc7d9 60%,#f3f3f3)"></div></div>
    <h3>Books</h3>
    <p>Lorem ipsum dolor sit amet, consectetuer adipiscing elit, sed diam nonummy nibh euismod tincidunt</p>
  </div>
  <div class="abs category" style="left:450px;top:805px">
    <div class="ring" style="border-color:#f26b6b"><div class="photo" role="img" aria-label="Photo of a pile of CD cases" style="background:radial-gradient(circle,#3aa0c8,#6b6b7a 60%,#f3f3f3)"></div></div>
    <h3>CD's</h3>
    <p>Lorem ipsum dolor sit amet, consectetuer adipiscing elit, sed diam nonummy nibh euismod tincidunt</p>
  </div>
  <div class="abs category" style="left:790px;top:805px">
    <div class="ring" style="border-color:#e93fbf"><div class="photo" role="img" aria-label="Photo of a swinging pocket-watch pendulum" style="background:radial-gradient(circle,#c9b48a,#e8e0d0 60%,#f6f6f6)"></div></div>
    <h3>Pendulums</h3>
    <p>Lorem ipsum dolor sit amet, consectetuer adipiscing elit, sed diam nonummy nibh euismod tincidunt</p>
  </div>

  <div class="abs rule" style="left:205px;top:1314px;width:790px"></div>
  <div class="abs ribbon" style="left:458px;top:1270px">Featured Products</div>
  <p class="abs products-lead">Lorem ipsum dolor sit amet, consectetuer adipiscing elit, sed diam nonummy nibh euismod tincidunt ut laoreet dolore magna aliquam erat volutpat.</p>

  <div class="abs product" style="left:144px;top:1495px">
    <div class="ring" style="border-color:#e6336e"><div class="photo" role="img" aria-label="Photo of a silver crystal bowl" style="background:radial-gradient(circle,#d8d8d8,#f2f2f2)"></div></div>
    <div class="tag" style="background:#e6336e"><span>laoreet dolore</span><span>$23</span></div>
  </div>
  <div class="abs product" style="left:331px;top:1495px">
    <div class="ring" style="border-color:#3ccfd6"><div class="photo" role="img" aria-label="Photo of stacked CDs" style="background:radial-gradient(circle,#b9a98a,#eee8dc)"></div></div>
    <div class="tag" style="background:#3ccfd6"><span>laoreet dolore</span><span>$23</span></div>
  </div>
  <div class="abs product" style="left:519px;top:1495px">
    <div class="ring" style="border-color:#b5d62e"><div class="photo" role="img" aria-label="Photo of a stack of books" style="background:radial-gradient(circle,#5a7fb0,#e9edf3)"></div></div>
    <div class="tag" style="background:#b5d62e"><span>laoreet dolore</span><span>$23</span></div>
  </div>
  <div class="abs product" style="left:705px;top:1495px">
    <div class="ring" style="border-color:#ea7a36"><div class="photo" role="img" aria-label="Photo of a pile of old books" style="background:radial-gradient(circle,#a58a70,#efe8e0)"></div></div>
    <div class="tag" style="background:#ea7a36"><span>laoreet dolore</span><span>$23</span></div>
  </div>
  <div class="abs product" style="left:895px;top:1495px">
    <div class="ring" style="border-color:#4cd964"><div class="photo" role="img" aria-label="Photo of a blue crystal cluster" style="background:radial-gradient(circle,#3b3fb8,#eceefa)"></div></div>
    <div class="tag" style="background:#4cd964"><span>laoreet dolore</span><span>$23</span></div>
  </div>

  <div class="abs product" style="left:332px;top:1760px">
    <div class="ring" style="border-color:#3f8fdc"><div class="photo" role="img" aria-label="Photo of a heart-shaped amethyst geode" style="background:radial-gradient(circle,#6a4a6e,#ece6ee)"></div></div>
    <div class="tag" style="background:#3f8fdc"><span>laoreet dolore</span><span>$23</span></div>
  </div>
  <div class="abs product" style="left:519px;top:1760px">
    <div class="ring" style="border-color:#22b8e8"><div class="photo" role="img" aria-label="Photo of red tumbled stones" style="background:radial-gradient(circle,#d0202c,#f4e6e6)"></div></div>
    <div class="tag" style="background:#22b8e8"><span>laoreet dolore</span><span>$23</span></div>
  </div>
  <div class="abs product" style="left:705px;top:1760px">
    <div class="ring" style="border-color:#b04fcf"><div class="photo" role="img" aria-label="Photo of a purple crystal point" style="background:radial-gradient(circle,#6b3fa8,#efe8f6)"></div></div>
    <div class="tag" style="background:#b04fcf"><span>laoreet dolore</span><span>$23</span></div>
  </div>

  <div class="abs rule" style="left:110px;top:2118px;width:980px"></div>
  <div class="abs ribbon" style="left:458px;top:2078px">Find Us</div>

  <div class="abs map" role="img" aria-label="Street map showing the shop location"></div>
  <div class="abs address">
    <span class="who">Mara L. Quinn</span>
    <span>88 Willow Lane</span>
    <span>Brightfield USA</span>
    <span>40417</span>
  </div>

  <section class="abs contact">
    <div class="field" style="left:51px;top:82px;width:237px;height:40px">Name</div>
    <div class="field" style="left:306px;top:82px;width:235px;height:40px">Email</div>
    <div class="field" style="left:51px;top:124px;width:490px;height:103px">Type Your Message</div>
  </section>
  <div class="abs btn-send">Send me your message</div>
  <div class="abs contact-copy">
    <h2>Lorem ipsum dolor sit amet.</h2>
    <p>consectetuer adipiscing elit, sed diam nonummy nibh euismod tincidunt ut laoreet dolore magna aliquam erat volutpat.</p>
    <ul>
      <li>Wuismod tindunt ut laoreet dolore magna</li>
      <li>Wuismod tindunt ut laoreet dolore magna</li>
      <li>Wuismod tindunt ut laoreet dolore magna</li>
    </ul>
  </div>

  <footer class="abs footer">Copyright ©2014 The Velvet Lantern</footer>
</div>
</body>
</html>
```